Marlow Fenwick Cocktail Menu design

I need a new cocktail menu for our bar 'Marlow Fenwick'.

The logo should read just the full Marlow Fenwick text logo at the top, and the small 'MF' part of the logo in the bottom corners.

The design should be slick, and modern to fit in with our club/bar branding which can be viewed on our social media or website www.marlowfenwick-example.co.uk

```html
<!DOCTYPE html>
<html lang="en">
<head>
<meta charset="utf-8">
<title>Marlow Fenwick – Cocktail Menus</title>
<link href="https://fonts.googleapis.com/css2?family=Oswald:wght@400;500;600;700&family=Roboto+Condensed:wght@400;500&display=swap" rel="stylesheet">
<style>
  :root{
    --canvas:#efefef;
    --ink:#0a0a0b;
    --paper:#ffffff;
    --muted:#cfcfd2;
    --rule:rgba(255,255,255,.45);
    --display:'Oswald', sans-serif;
    --body:'Roboto Condensed', sans-serif;
  }
  *{box-sizing:border-box;margin:0;padding:0}
  html,body{width:783px;height:1200px;overflow:hidden}
  body{background:var(--canvas);position:relative;font-family:var(--body);color:var(--paper)}

  .menu{position:absolute;left:166px;width:450px;height:581px;background:var(--ink);overflow:hidden}
  .menu--long-islands{top:12px}
  .menu--classics{top:607px}

  .backdrop{position:absolute;inset:0}
  .menu--long-islands .backdrop{
    background:
      radial-gradient(ellipse 60% 30% at 35% 0%, rgba(190,190,195,.35), transparent 70%),
      linear-gradient(180deg, #0b0b0c 0%, #0d0e10 45%, #1a2129 72%, #2a3641 86%, #1b242d 100%);
  }
  .menu--classics .backdrop{
    background:
      radial-gradient(ellipse 60% 30% at 35% 0%, rgba(190,190,195,.3), transparent 70%),
      linear-gradient(180deg, #0b0b0c 0%, #0a0a0b 100%);
  }
  .feature-photo{position:absolute;left:239px;top:179px;width:211px;height:373px;
    background:
      radial-gradient(circle at 40% 28%, rgba(222,98,40,.85) 0 16%, transparent 30%),
      radial-gradient(circle at 78% 62%, rgba(200,70,60,.75) 0 12%, transparent 26%),
      radial-gradient(circle at 30% 70%, rgba(226,226,230,.5) 0 12%, transparent 30%),
      radial-gradient(ellipse at 50% 35%, rgba(140,160,175,.55), transparent 70%);
  }

  .frame{position:absolute;inset:0;width:450px;height:581px}

  .brand{position:absolute;left:41px;top:30px;text-align:center}
  .brand-name{font-family:var(--display);font-weight:600;font-size:26px;line-height:1;letter-spacing:.2px;text-transform:uppercase}
  .brand-tag{font-family:var(--display);font-size:6.5px;letter-spacing:3px;margin-top:3px;font-weight:500}

  .title{position:absolute;left:41px;font-family:var(--display);font-weight:600;text-transform:uppercase;line-height:1;letter-spacing:-.5px}
  .title--outline{color:transparent;-webkit-text-stroke:1.1px var(--paper);font-weight:500}

  .section-tag{position:absolute;left:41px;width:158px;height:28px;border:2px solid var(--paper);display:flex;font-family:var(--display);font-weight:500;text-transform:uppercase;font-size:18px;line-height:24px}
  .section-tag__key{background:var(--paper);color:var(--ink);padding:0 7px}
  .section-tag__rest{flex:1;padding-left:6px;color:var(--paper)}
  .section-tag--centered{justify-content:center;border-left-width:12px;border-right-width:12px;background:var(--ink)}

  .item{position:absolute;left:41px;width:201px}
  .item-head{display:flex;align-items:flex-end;font-family:var(--display);font-weight:500;font-size:9.5px;line-height:1;text-transform:uppercase}
  .item-leader{flex:1;border-bottom:.6px solid var(--rule);margin:0 6px 3px 4px}
  .item-desc{font-size:6.6px;line-height:1.35;color:var(--muted);margin-top:2px}

  .photo-ring{position:absolute;border-radius:50%;border:1px solid rgba(255,255,255,.75)}
  .photo-circle{position:absolute;border-radius:50%;border:1.5px solid var(--paper)}
  .photo-circle--beach{left:282px;top:182px;width:118px;height:118px;
    background:linear-gradient(180deg,#e9d6c4 0%,#d7a987 45%,#8d7767 70%,#c8c4bd 100%)}
  .photo-circle--club{left:293px;top:290px;width:96px;height:96px;
    background:radial-gradient(circle at 40% 35%,#b461e0 0%,#5b2aa8 45%,#1a1330 100%)}

  .offer{position:absolute;left:289px;top:401px;width:114px;height:27px;border:1.5px solid var(--paper);display:flex;align-items:stretch;font-family:var(--display)}
  .offer-price{background:var(--paper);color:var(--ink);display:flex;align-items:center;padding:0 4px 0 2px;font-weight:600;font-size:15px}
  .offer-all{font-size:5px;writing-mode:vertical-rl;transform:rotate(180deg);margin-right:2px;font-weight:500}
  .offer-when{flex:1;display:flex;align-items:center;justify-content:center;font-size:13px;letter-spacing:.5px;font-weight:400}
  .happy-hour{position:absolute;left:289px;top:434px;font-family:var(--display);font-weight:700;font-size:29px;line-height:.95;text-transform:uppercase;letter-spacing:-.5px}
  .pint-photo{position:absolute;left:374px;top:437px;width:29px;height:55px;border-radius:3px 3px 4px 4px;
    background:linear-gradient(180deg,#f4efe6 0 14%,#e6a53a 14%,#c97a1c 100%)}
  .happy-days{position:absolute;left:289px;top:496px;font-size:7px;letter-spacing:.2px;text-transform:uppercase}
  .happy-days b{font-weight:500}

  .sign-off{position:absolute;left:37px;top:524px;display:flex;align-items:flex-end;gap:12px}
  .sign-off__mark{font-family:var(--display);font-weight:700;font-size:28px;line-height:1;letter-spacing:-.5px}
  .sign-off__web{font-size:9px;line-height:1;margin-bottom:1px}
</style>
</head>
<body>

<!-- Long Islands menu -->
<section class="menu menu--long-islands">
  <div class="backdrop" role="img" aria-label="Moody dark background with a soft spotlight beam at the top and a stormy rocky sea shore along the bottom"></div>

  <svg class="frame" viewBox="0 0 450 581" aria-hidden="true">
    <polyline points="218,49 426,49 426,547 238,547" fill="none" stroke="#fff" stroke-width="1"/>
  </svg>

  <header class="brand">
    <div class="brand-name">Marlow Fenwick</div>
    <div class="brand-tag">BAR . CLUB . FOOD</div>
  </header>

  <h1 class="title" style="top:90px;font-size:44px">MF’s Long List Of</h1>
  <h2 class="title title--outline" style="top:137px;font-size:44px">‘Long Islands’</h2>

  <div class="section-tag" style="top:198px"><span class="section-tag__key">Long</span><span class="section-tag__rest">Island Iced</span></div>
  <div class="item" style="top:236px">
    <div class="item-head"><span>Tea</span><span class="item-leader"></span><span>£9.50</span></div>
    <p class="item-desc">Vodka, Gin, Rum, Tequila, Orange Liqueur, Lemon &amp; Coke</p>
  </div>

  <div class="section-tag" style="top:276px"><span class="section-tag__key">Long</span><span class="section-tag__rest">Beach Iced</span></div>
  <div class="item" style="top:316px">
    <div class="item-head"><span>Tea</span><span class="item-leader"></span><span>£9.50</span></div>
    <p class="item-desc">Vodka, Gin, Rum, Tequila, Orange Liqueur<br>Lemon &amp; Cranberry</p>
  </div>
  <div class="item" style="top:354px">
    <div class="item-head"><span>AMF</span><span class="item-leader"></span><span>£9.50</span></div>
    <p class="item-desc">Vodka, Gin, Rum, Tequila, Blue Curacao<br>Lemon &amp; Lemonade</p>
  </div>
  <div class="item" style="top:393px">
    <div class="item-head"><span>Tokyo Iced Tea</span><span class="item-leader"></span><span>£9.50</span></div>
    <p class="item-desc">Vodka, Gin, Rum, Tequila, Melon Liqueur,<br>Lemon &amp; Lemonade</p>
  </div>
  <div class="item" style="top:433px">
    <div class="item-head"><span>Tiki Iced Tea</span><span class="item-leader"></span><span>£9.50</span></div>
    <p class="item-desc">Vodka, Gin, Coconut Rum, Tequila, Orange<br>Liqueur, Lime &amp; Pineapple</p>
  </div>
  <div class="item" style="top:474px">
    <div class="item-head"><span>Long Island Iced Coffee</span><span class="item-leader"></span><span>£9.50</span></div>
    <p class="item-desc">Vodka, Gin, Rum, Tequila, Dunmore Cream, Milk,<br>Salted Caramel Syrup &amp; Espresso</p>
  </div>

  <div class="photo-ring" style="left:279px;top:179px;width:124px;height:124px"></div>
  <div class="photo-circle photo-circle--beach" role="img" aria-label="Photo of friends gathered at a beach bar at sunset under festoon lights"></div>
  <div class="photo-ring" style="left:290px;top:287px;width:102px;height:102px"></div>
  <div class="photo-circle photo-circle--club" role="img" aria-label="Photo of a crowded club night lit in purple with a DJ booth"></div>

  <div class="offer"><span class="offer-price"><span class="offer-all">ALL</span>£4.95</span><span class="offer-when">DURING</span></div>
  <div class="happy-hour">Happy<br>Hour</div>
  <div class="pint-photo" role="img" aria-label="Photo of a pint of lager"></div>
  <p class="happy-days">Sunday to Friday . <b>6PM – 8PM</b></p>

  <footer class="sign-off">
    <span class="sign-off__mark">MF’s</span>
    <span class="sign-off__web">www.marlowfenwick-example.co.uk</span>
  </footer>
</section>

<!-- Classic cocktails menu -->
<section class="menu menu--classics">
  <div class="backdrop" role="img" aria-label="Dark background with a soft spotlight beam at the top"></div>
  <div class="feature-photo" role="img" aria-label="Photo of an orange cocktail in a coupe wrapped in smoke, with an iced glass, a gin bottle, mango, lime and chillies"></div>

  <svg class="frame" viewBox="0 0 450 581" aria-hidden="true">
    <polyline points="218,49 426,49 426,547 238,547" fill="none" stroke="#fff" stroke-width="1"/>
  </svg>

  <header class="brand">
    <div class="brand-name">Marlow Fenwick</div>
    <div class="brand-tag">BAR . CLUB . FOOD</div>
  </header>

  <h1 class="title" style="top:88px;font-size:57px;font-weight:700">Classic</h1>
  <h2 class="title title--outline" style="top:145px;font-size:58px">Cocktails</h2>

  <div class="section-tag section-tag--centered" style="top:228px"><span class="section-tag__rest" style="flex:none;padding:0">Arancio</span></div>

  <div class="item" style="top:272px">
    <div class="item-head"><span>Spritz</span><span class="item-leader"></span><span>£8.50</span></div>
    <p class="item-desc">Arancio, Prosecco &amp; Soda</p>
  </div>
  <div class="item" style="top:303px">
    <div class="item-head"><span>Margarita</span><span class="item-leader"></span><span>£7.95</span></div>
    <p class="item-desc">Tequila, Orange Liqueur &amp; Lime</p>
  </div>
  <div class="item" style="top:334px">
    <div class="item-head"><span>Pornstar Martini</span><span class="item-leader"></span><span>£8.50</span></div>
    <p class="item-desc">Vanilla Vodka, Maracu, Passion Fruit<br>Puree, Pineapple &amp; Lime</p>
  </div>
  <div class="item" style="top:371px">
    <div class="item-head"><span>Espresso Martini</span><span class="item-leader"></span><span>£8.50</span></div>
    <p class="item-desc">Vanilla Vodka, Coffee Liqueur &amp; Espresso</p>
  </div>
  <div class="item" style="top:401px">
    <div class="item-head"><span>Gin Spritz</span><span class="item-leader"></span><span>£7.95</span></div>
    <p class="item-desc">Pink Gin, Strawberry Syrup, Prosecco &amp;<br>Lemonade</p>
  </div>
  <div class="item" style="top:439px">
    <div class="item-head"><span>Mai Tai</span><span class="item-leader"></span><span>£8.95</span></div>
    <p class="item-desc">Dark Rum, White Rum, Orange Liqueur,<br>Orgeat, Lime &amp; Pineapple</p>
  </div>
  <div class="item" style="top:476px">
    <div class="item-head"><span>Whiskey Sour</span><span class="item-leader"></span><span>£8.95</span></div>
    <p class="item-desc">Bourbon Whiskey, Lemon &amp; Egg White</p>
  </div>

  <footer class="sign-off">
    <span class="sign-off__mark">MF’s</span>
    <span class="sign-off__web">www.marlowfenwick-example.co.uk</span>
  </footer>
</section>

</body>
</html>
```